Flyer for Aluminium recycling business

We are a startup aluminium recycling business. We don’t have a logo yet. I’ve attached a flyer created by one of our sales people but it’s a bit average and we need something a bit more modern and slick. You have creative license to completely change everything - as long as the information being communicated is the same.

Target Market(s)

Hospitality, Hotels, Apartment blocks, malls etcs

Industry/Entity Type

Aluminium recycling

Requirements
Must have
• the wording
Nice to have
• you have free license on design aspect

```html
<!DOCTYPE html>
<html lang="en">
<head>
<meta charset="utf-8">
<title>Brightloop Metals – Aluminium Recycling</title>
<link rel="stylesheet" href="https://fonts.googleapis.com/css2?family=Plus+Jakarta+Sans:wght@400;500;700;800&display=swap">
<style>
  :root {
    --forest: #0f4a2a;
    --leaf: #2a9d48;
    --lime: #b9e56e;
    --mint: #eef6f0;
    --mint-line: #d3e8d9;
    --ink: #1d2b23;
    --ink-soft: #44564b;
    --white: #ffffff;
    --art-dark: #2f3a33;
  }
  * { box-sizing: border-box; margin: 0; padding: 0; }
  html, body { width: 848px; height: 1200px; overflow: hidden; background: var(--white); }
  body { font-family: "Plus Jakarta Sans", Helvetica, Arial, sans-serif; color: var(--ink); }
  .flyer { position: relative; width: 848px; height: 1200px; }

  /* Masthead */
  .masthead { position: absolute; left: 0; top: 0; width: 848px; height: 232px; background: var(--forest); color: var(--white); padding: 52px 48px 0; }
  .brand { display: flex; align-items: center; gap: 16px; }
  .brand__dot { width: 22px; height: 22px; border-radius: 50%; background: var(--lime); flex: none; }
  .brand__name { font-size: 46px; font-weight: 800; letter-spacing: 1px; line-height: 1; }
  .masthead__tagline { margin-top: 14px; font-size: 22px; font-weight: 500; line-height: 1.2; color: #d9ecd f; color: #dcefe1; }
  .masthead__rule { margin-top: 26px; height: 1px; background: rgba(255,255,255,0.22); }
  .masthead__promise { margin-top: 16px; font-size: 16px; font-weight: 700; color: var(--lime); line-height: 1.3; }

  /* Section titles */
  .section-title { position: absolute; left: 48px; font-size: 30px; font-weight: 800; letter-spacing: 0.5px; color: var(--forest); line-height: 1; }
  .section-title::after { content: ""; display: inline-block; width: 48px; height: 4px; border-radius: 2px; background: var(--leaf); margin-left: 14px; vertical-align: middle; }
  .steps-title { top: 264px; }
  .accepted-title { top: 722px; }

  /* Steps */
  .steps { position: absolute; left: 48px; top: 310px; width: 752px; list-style: none; display: flex; flex-direction: column; gap: 7px; }
  .step { height: 74px; background: var(--mint); border-radius: 14px; display: flex; align-items: center; gap: 16px; padding: 0 20px 0 14px; }
  .step__num { flex: none; width: 38px; height: 38px; border-radius: 50%; background: var(--leaf); color: var(--white); font-size: 17px; font-weight: 800; display: flex; align-items: center; justify-content: center; }
  .step__art { flex: none; width: 112px; height: 54px; border-radius: 10px; }
  .step__text { font-size: 15px; font-weight: 500; line-height: 1.35; color: var(--ink); }

  /* Accepted items */
  .items { position: absolute; left: 48px; top: 772px; width: 752px; list-style: none; display: flex; gap: 14px; }
  .item { flex: 1; height: 206px; background: var(--mint); border: 1px solid var(--mint-line); border-radius: 16px; padding: 10px; text-align: center; }
  .item__art { height: 100px; border-radius: 12px; background: var(--art-dark); display: flex; align-items: center; justify-content: center; }
  .item__art span { display: block; width: 64px; height: 64px; border-radius: 10px; }
  .item__caption { margin-top: 12px; font-size: 13.5px; font-weight: 700; line-height: 1.33; color: var(--forest); }

  /* Contact */
  .contact { position: absolute; left: 0; top: 1040px; width: 848px; height: 160px; background: var(--forest); color: var(--white); padding: 0 48px; display: flex; align-items: center; justify-content: space-between; }
  .contact__call { display: flex; flex-direction: column; }
  .contact__lead { font-size: 20px; font-weight: 500; color: #dcefe1; line-height: 1.2; }
  .contact__phone { font-size: 44px; font-weight: 800; color: var(--lime); letter-spacing: 0.5px; line-height: 1.15; }
  .contact__email { font-size: 23px; font-weight: 700; line-height: 1.2; padding: 14px 22px; border: 1.5px solid rgba(255,255,255,0.35); border-radius: 40px; }
</style>
</head>
<body>
<main class="flyer">
  <header class="masthead">
    <div class="brand">
      <span class="brand__dot" aria-hidden="true"></span>
      <h1 class="brand__name">BRIGHTLOOP METALS</h1>
    </div>
    <p class="masthead__tagline">Playing the fair aluminium recycling game for good</p>
    <div class="masthead__rule" aria-hidden="true"></div>
    <p class="masthead__promise">Our partnership with you is based on common sense, mutual gain and a better tomorrow</p>
  </header>

  <h2 class="section-title steps-title">IT’S SIMPLE</h2>
  <ol class="steps">
    <li class="step">
      <span class="step__num">1</span>
      <div class="step__art" role="img" aria-label="Illustration of a worker wheeling a green recycling bin" style="background:linear-gradient(135deg,#cfe6d5,#7fbf8f)"></div>
      <p class="step__text">We bring you a free bin</p>
    </li>
    <li class="step">
      <span class="step__num">2</span>
      <div class="step__art" role="img" aria-label="Illustration of a worker dropping a bag into an open green bin" style="background:linear-gradient(135deg,#cfe6d5,#5ea873)"></div>
      <p class="step__text">You throw all and any aluminum waste into bin - no need to super -clean it. Try to compact / squash the aluminium as much as possible.</p>
    </li>
    <li class="step">
      <span class="step__num">3</span>
      <div class="step__art" role="img" aria-label="Illustration of a bin being loaded into an orange collection truck" style="background:linear-gradient(135deg,#cfe6d5,#f0c27f)"></div>
      <p class="step__text">We collect the bin at no charge</p>
    </li>
    <li class="step">
      <span class="step__num">4</span>
      <div class="step__art" role="img" aria-label="Crumpled aluminium foil turning into recycled material at a plant" style="background:linear-gradient(135deg,#d4d6d8,#8fcf98)"></div>
      <p class="step__text">We turn the aluminium waste into a desirable resource</p>
    </li>
    <li class="step">
      <span class="step__num">5</span>
      <div class="step__art" role="img" aria-label="Payment changing hands followed by a checklist report" style="background:linear-gradient(135deg,#2a9d48,#dfeef2)"></div>
      <p class="step__text">We pay you however much of that resource your waste has generated - and give you a report on that, so you can see how good you are.</p>
    </li>
  </ol>

  <h2 class="section-title accepted-title">EXAMPLES OF WHAT WE CAN TAKE</h2>
  <ul class="items">
    <li class="item">
      <div class="item__art"><span role="img" aria-label="Assorted drink cans" style="background:linear-gradient(135deg,#f07a2a,#c63a3a 50%,#c565d8)"></span></div>
      <p class="item__caption">Used beverage cans - any</p>
    </li>
    <li class="item">
      <div class="item__art"><span role="img" aria-label="Scrunched tinfoil" style="background:linear-gradient(135deg,#ececec,#9a9a9a)"></span></div>
      <p class="item__caption">Tinfoil - scrunched, crusty, burned or dirty</p>
    </li>
    <li class="item">
      <div class="item__art"><span role="img" aria-label="Stacked aluminium takeaway containers" style="background:linear-gradient(135deg,#dcdcdc,#a8a8a8)"></span></div>
      <p class="item__caption">Aluminium takeaway containers</p>
    </li>
    <li class="item">
      <div class="item__art"><span role="img" aria-label="Gold wine bottle screw caps" style="background:linear-gradient(135deg,#e6d79a,#a89254)"></span></div>
      <p class="item__caption">Wine Bottles screw tops (Collars - if you can get them off)</p>
    </li>
    <li class="item">
      <div class="item__art"><span role="img" aria-label="Tin can with tear-off lid" style="background:linear-gradient(135deg,#f4f4f4,#a9a9a9)"></span></div>
      <p class="item__caption">Tear–off can lids</p>
    </li>
  </ul>

  <footer class="contact">
    <div class="contact__call">
      <span class="contact__lead">Call us</span>
      <span class="contact__phone">020-555-0148</span>
    </div>
    <span class="contact__email">join@brightloopmetals.co.nz</span>
  </footer>
</main>
</body>
</html>
```